Wagely Allies Business Card Design

We need a business card designed around our new logo. The business card should be modern in design & should communicate success, confidence, power, sophistication. The target market is young business professionals. This is for a human resource & payroll outsourcing business.

```html
<!DOCTYPE html>
<html lang="en">
<head>
<meta charset="utf-8">
<meta name="format-detection" content="telephone=no, email=no, address=no">
<title>Wagely Allies Stationery</title>
<link href="https://fonts.googleapis.com/css2?family=Lato:wght@400;700&display=swap" rel="stylesheet">
<style>
  :root {
    --backdrop: #3b3939;
    --paper: #ffffff;
    --ink: #1a1a1a;
    --band: #0d0d0d;
    --accent: #e0222b;
    --light-text: #ffffff;
    --watermark-grey: #e9e9e9;
    --watermark-pink: #f5b9bb;
  }
  * { margin: 0; padding: 0; box-sizing: border-box; }
  html, body { width: 1200px; height: 955px; overflow: hidden; }
  body {
    background: var(--backdrop);
    font-family: "Lato", Arial, sans-serif;
    position: relative;
  }
  .plain-text { color: inherit; text-decoration: none; }

  /* Letterhead */
  .letterhead {
    position: absolute;
    left: 236px; top: 138px;
    width: 490px; height: 682px;
    background: var(--paper);
    overflow: hidden;
  }
  .letterhead .brand-name {
    position: absolute;
    left: 16px; top: 32px;
    font-size: 27px;
    font-weight: 400;
    color: var(--ink);
  }
  .letterhead .brand-watermark {
    position: absolute;
    left: 0; right: 0; top: 300px;
    text-align: center;
    font-size: 58px;
    font-weight: 700;
    color: var(--watermark-grey);
  }
  .letterhead .phone-list {
    position: absolute;
    left: 312px; top: 30px;
    padding-left: 14px;
    border-left: 2px solid var(--ink);
    list-style: none;
  }
  .letterhead .phone-list li {
    display: flex; align-items: center; gap: 10px;
    font-size: 14px; line-height: 16px; color: var(--ink);
  }
  .letterhead .phone-list svg { width: 12px; height: 12px; fill: var(--accent); }
  .letterhead .footer-wave {
    position: absolute; left: 0; bottom: 0;
    width: 490px; height: 95px; display: block;
  }
  .letterhead .address {
    position: absolute;
    right: 36px; bottom: 20px;
    display: flex; align-items: center; gap: 10px;
    font-size: 17px; color: var(--light-text);
  }
  .letterhead .address svg { width: 15px; height: 18px; fill: var(--accent); }

  /* Business cards */
  .card {
    position: absolute;
    left: 787px;
    width: 299px; height: 170px;
    background: var(--paper);
    border-radius: 14px;
    overflow: hidden;
  }
  .card-front { top: 143px; }
  .card-back { top: 328px; }

  .card-front .brand-name {
    position: absolute;
    left: 16px; top: 22px;
    font-size: 22px; font-weight: 400;
    color: var(--ink);
  }
  .card-front .holder {
    position: absolute; right: 12px; top: 12px; text-align: right;
  }
  .card-front .holder-name { font-size: 13px; font-weight: 700; color: var(--ink); }
  .card-front .holder-role { font-size: 7px; color: var(--ink); }
  .card-front .card-wave {
    position: absolute; left: 0; bottom: 0;
    width: 299px; height: 105px; display: block;
  }
  .card-front .contact-list {
    position: absolute; right: 12px; top: 93px;
    list-style: none; text-align: right;
  }
  .card-front .contact-list li {
    display: flex; justify-content: flex-end; align-items: center; gap: 6px;
    font-size: 8px; line-height: 16px; color: var(--light-text);
  }
  .card-front .contact-list svg { width: 8px; height: 8px; fill: var(--light-text); }

  .card-back .brand-mark {
    position: absolute;
    left: 0; right: 0; top: 70px;
    text-align: center;
    font-size: 24px; font-weight: 700;
    color: var(--watermark-pink);
  }
</style>
</head>
<body>

<section class="letterhead">
  <div class="brand-name">Wagely Allies</div>
  <ul class="phone-list">
    <li><svg viewBox="0 0 24 24"><path d="M6.6 10.8a15 15 0 0 0 6.6 6.6l2.2-2.2a1 1 0 0 1 1-.25 11.4 11.4 0 0 0 3.6.57 1 1 0 0 1 1 1V20a1 1 0 0 1-1 1A17 17 0 0 1 3 4a1 1 0 0 1 1-1h3.5a1 1 0 0 1 1 1c0 1.25.2 2.45.57 3.57a1 1 0 0 1-.25 1z"/></svg>00000000000</li>
    <li><svg viewBox="0 0 24 24"><path d="M6.6 10.8a15 15 0 0 0 6.6 6.6l2.2-2.2a1 1 0 0 1 1-.25 11.4 11.4 0 0 0 3.6.57 1 1 0 0 1 1 1V20a1 1 0 0 1-1 1A17 17 0 0 1 3 4a1 1 0 0 1 1-1h3.5a1 1 0 0 1 1 1c0 1.25.2 2.45.57 3.57a1 1 0 0 1-.25 1z"/></svg>00000000000</li>
    <li><svg viewBox="0 0 24 24"><path d="M6.6 10.8a15 15 0 0 0 6.6 6.6l2.2-2.2a1 1 0 0 1 1-.25 11.4 11.4 0 0 0 3.6.57 1 1 0 0 1 1 1V20a1 1 0 0 1-1 1A17 17 0 0 1 3 4a1 1 0 0 1 1-1h3.5a1 1 0 0 1 1 1c0 1.25.2 2.45.57 3.57a1 1 0 0 1-.25 1z"/></svg>00000000000</li>
  </ul>

  <div class="brand-watermark" aria-hidden="true">Wagely Allies</div>

  <svg class="footer-wave" viewBox="0 0 490 95" preserveAspectRatio="none" aria-hidden="true">
    <path d="M0,52 C140,48 260,10 490,0 L490,95 L0,95 Z" fill="var(--band)"/>
    <path d="M0,42 C90,44 170,36 230,22 C160,40 80,50 0,50 Z" fill="var(--accent)"/>
    <path d="M60,70 C200,66 300,22 430,6 C300,28 200,60 60,74 Z" fill="var(--light-text)"/>
  </svg>
  <div class="address">
    <svg viewBox="0 0 24 30"><path d="M12 0a11 11 0 0 0-11 11c0 8 11 19 11 19s11-11 11-19A11 11 0 0 0 12 0zm0 15a4 4 0 1 1 0-8 4 4 0 0 1 0 8z"/></svg>
    <span class="plain-text">level 12 Harbour Court</span>
  </div>
</section>

<section class="card card-front">
  <div class="brand-name">Wagely Allies</div>
  <div class="holder">
    <div class="holder-name">TARIQ NOOR</div>
    <div class="holder-role">Designer</div>
  </div>
  <svg class="card-wave" viewBox="0 0 299 105" preserveAspectRatio="none" aria-hidden="true">
    <path d="M0,55 C80,60 140,20 260,0 L299,0 L299,105 L0,105 Z" fill="var(--band)"/>
    <path d="M0,44 C50,50 90,42 140,26 C100,46 50,58 0,56 Z" fill="var(--accent)"/>
    <path d="M30,82 C110,76 160,18 255,4 C170,26 110,76 30,86 Z" fill="var(--light-text)"/>
  </svg>
  <ul class="contact-list">
    <li><span class="plain-text">00000000000</span><svg viewBox="0 0 24 24"><path d="M6.6 10.8a15 15 0 0 0 6.6 6.6l2.2-2.2a1 1 0 0 1 1-.25 11.4 11.4 0 0 0 3.6.57 1 1 0 0 1 1 1V20a1 1 0 0 1-1 1A17 17 0 0 1 3 4a1 1 0 0 1 1-1h3.5a1 1 0 0 1 1 1c0 1.25.2 2.45.57 3.57a1 1 0 0 1-.25 1z"/></svg></li>
    <li><span class="plain-text">hello@wagelyallies.com</span><svg viewBox="0 0 24 24"><path d="M2 5h20v14H2z M2 5l10 8 10-8" fill="none" stroke="#fff" stroke-width="3"/></svg></li>
    <li><span class="plain-text">www.wagelyallies.com</span><svg viewBox="0 0 24 24"><circle cx="12" cy="12" r="9" fill="none" stroke="#fff" stroke-width="3"/><path d="M3 12h18M12 3c4 5 4 13 0 18c-4-5-4-13 0-18" fill="none" stroke="#fff" stroke-width="2"/></svg></li>
    <li><span class="plain-text">level 12 Harbour Court</span><svg viewBox="0 0 24 30"><path d="M12 0a11 11 0 0 0-11 11c0 8 11 19 11 19s11-11 11-19A11 11 0 0 0 12 0zm0 15a4 4 0 1 1 0-8 4 4 0 0 1 0 8z"/></svg></li>
  </ul>
</section>

<section class="card card-back">
  <div class="brand-mark">Wagely Allies</div>
</section>

</body>
</html>
```